Aviation: Overcast Study Guide Book Cover

We need a book cover (front and back) designed for an Instrument Flight Rules (IFR) study guide used by helicopter and airplane pilots to obtain an instrument rating for a helicopter or airplane. Below is the title and subtitles.

TITLE: OVERCAST STUDY GUIDE
SUBTITLE 1: Checkride Preparation for Airplane and Helicopter Pilots
SUBTITLE 2: Prepare for your Instrument Rating with Confidence

We have also upload recommended text to be included on the back cover. In addition, we included images of similar book covers that we like and ones that we do not like. Below are links to two others books by the author.

https://www.bookvarro.example/Rotorcraft-Exam-Handbook-oral-review/dp/507214638K
https://www.bookvarro.example/Manual-Floatwing-Handling-Lionel-Quarrick/dp/5093742816

Flight students

Aviation

• helicopter and airplane

```html
<!DOCTYPE html>
<html lang="en">
<head>
<meta charset="utf-8">
<title>Overcast Study Guide – Cover Spread</title>
<link href="https://fonts.googleapis.com/css2?family=Montserrat:wght@400;500;600;700;800&family=Playfair+Display:wght@400&display=swap" rel="stylesheet">
<style>
  :root {
    --page-bg: #dfe4e8;
    --ink-dark: #1b1b1c;
    --ink-mid: #2c2c2e;
    --ink-soft: #3a3a3d;
    --accent: #fcc433;
    --text-light: #f2f2f2;
    --text-muted: #d8d8d8;
    --photo-top: #3a3f49;
    --photo-bottom: #15171b;
  }
  * { box-sizing: border-box; margin: 0; padding: 0; }
  html, body { width: 848px; height: 1200px; overflow: hidden; }
  body {
    background: var(--page-bg);
    font-family: "Montserrat", sans-serif;
    position: relative;
  }
  .spread {
    position: absolute;
    left: 20px; top: 343px;
    width: 808px; height: 514px;
    display: flex;
    border: 1px solid #55585c;
  }

  /* Back cover */
  .back-cover {
    width: 396px; height: 100%;
    position: relative;
    background: linear-gradient(180deg, var(--ink-mid) 0%, var(--ink-dark) 100%);
    color: var(--text-light);
    overflow: hidden;
  }
  .back-photo {
    position: absolute; left: 0; right: 0; top: 340px; bottom: 40px;
    background: linear-gradient(180deg, rgba(21,23,27,0) 0%, #2a2e35 45%, #1c1f24 100%);
    opacity: .9;
  }
  .back-content { position: relative; padding: 33px 32px 0 33px; }
  .back-heading {
    color: var(--accent);
    font-weight: 600;
    font-size: 9px;
    margin-bottom: 6px;
  }
  .back-para {
    font-size: 5.6px;
    line-height: 1.95;
    color: var(--text-muted);
    margin-bottom: 13px;
  }
  .topic-list {
    list-style: none;
    display: grid;
    grid-template-columns: 106px 114px 1fr;
    row-gap: 5px;
    font-size: 7px;
    color: var(--text-muted);
    margin-top: -4px;
  }
  .topic-list li::before { content: "• "; }
  .back-divider {
    height: 5px; background: var(--accent);
    margin: 18px 0 13px;
  }
  .author-bio {
    font-size: 8.4px;
    line-height: 1.72;
    color: var(--text-light);
  }
  .author-bio .book-link { color: var(--accent); }
  .back-band {
    position: absolute; left: 0; right: 0; bottom: 0;
    height: 40px; background: var(--accent);
  }

  /* Spine */
  .spine {
    width: 16px; height: 100%;
    background: var(--ink-dark);
    position: relative;
    border-left: 1px dashed #c9c9c9;
    border-right: 1px dashed #c9c9c9;
  }
  .spine-text {
    position: absolute; left: 50%; top: 322px;
    transform: translateX(-50%) rotate(90deg);
    transform-origin: center top;
    white-space: nowrap;
    font-size: 5.4px;
    font-weight: 600;
    display: flex; gap: 14px;
    width: 0;
  }
  .spine-title { color: var(--text-light); }
  .spine-author { color: var(--accent); }

  /* Front cover */
  .front-cover {
    flex: 1; height: 100%;
    position: relative;
    background: linear-gradient(180deg, var(--ink-mid) 0%, var(--ink-dark) 100%);
    overflow: hidden;
  }
  .author-band {
    height: 40px; background: var(--accent);
    display: flex; align-items: center; justify-content: center;
    font-weight: 700; font-size: 12.5px; color: var(--ink-dark);
  }
  .title-band {
    height: 70px;
    background: linear-gradient(90deg, #161617, #2d2d30);
    display: flex; align-items: center; justify-content: center;
  }
  .book-title {
    color: #fff;
    font-weight: 700;
    font-size: 23px;
    letter-spacing: 3.6px;
    white-space: nowrap;
  }
  .title-rule { height: 5px; background: var(--accent); }
  .cover-photo {
    height: 298px;
    background: radial-gradient(ellipse at 50% 35%, #5c6370 0%, var(--photo-top) 35%, var(--photo-bottom) 100%);
  }
  .subtitle-band {
    height: 38px; background: var(--accent);
    display: flex; align-items: center; justify-content: center;
    font-size: 11px; font-weight: 500; color: var(--ink-dark);
  }
  .tagline {
    font-family: "Playfair Display", serif;
    color: var(--text-light);
    font-size: 11.2px;
    text-align: center;
    margin-top: 17px;
  }
</style>
</head>
<body>
  <div class="spread">
    <section class="back-cover">
      <div class="back-photo" role="img" aria-label="Darkened photo of a pilot in a jet cockpit reaching for the overhead panel"></div>
      <div class="back-content">
        <h2 class="back-heading">Prepare for your IFR check ride with confidence</h2>
        <p class="back-para">Becoming an instrument rated pilot is one of the most challenging ratings to obtain. This guide helps prepare you to pass your IFR check ride with confidence. The question-and-answer format is easy to follow and provides detailed explanations for expanded knowledge.</p>
        <h2 class="back-heading">Includes Helicopter and Airplane Specific Content</h2>
        <p class="back-para">This guide is designed to prepare an airplane or helicopter pilot the oral portion of the IFR checkride. Unlike other resources, this guide specifically addresses the differences with IFR flight in helicopters. As a dual rated pilot, the author ensures to identify areas of differences between the two categories of IFR flight. The following concepts are addressed within the guide.</p>
        <ul class="topic-list">
          <li>Preflight Actions</li>
          <li>Enroute Procedures</li>
          <li>Aeromedical Factors</li>
          <li>General IFR Concepts</li>
          <li>Weather Fundamentals</li>
          <li>Weather Fundamentals</li>
          <li>Departure Procedures</li>
          <li>IFR Emergences</li>
          <li>Risk Management</li>
        </ul>
        <div class="back-divider"></div>
        <p class="author-bio">Lionel Quarrick is ATP rated pilot, helicopter and fixed-wing instructor. Lionel is the owner and operator Northvane Holdings, LLC which does business as Hoverline Aviation and Pelican Reach Aviation. Hoverline Aviation provides primary helicopter flight instruction, while Pelican Reach Aviation provides seaplane flight instruction and tours. In addition to instructing, he has authored other books to include <span class="book-link">Rotorcraft Exam Handbook</span>, and <span class="book-link">Manual of Floatwing Handling</span>. Prior to learning to fly, Lionel spent several years in the military as a Special Warfare Combat Craft Crewman in the U.S. Navy, Ranger-qualified infantry officer in the U.S. Army.</p>
      </div>
      <div class="back-band"></div>
    </section>

    <aside class="spine">
      <div class="spine-text">
        <span class="spine-title">OVERCAST STUDY GUIDE</span>
        <span class="spine-author">Lionel Quarrick</span>
      </div>
    </aside>

    <section class="front-cover">
      <div class="author-band">Lionel Quarrick</div>
      <div class="title-band"><h1 class="book-title">OVERCAST STUDY GUIDE</h1></div>
      <div class="title-rule"></div>
      <div class="cover-photo" role="img" aria-label="Photo of a pilot seated in a jet cockpit reaching up to the overhead switch panel"></div>
      <div class="subtitle-band">Checkride Preparation for Airplane and Helicopter Pilots</div>
      <p class="tagline">Prepare for your Instrument Rating with Confidence</p>
    </section>
  </div>
</body>
</html>
```